Liquor Label / Aguardiente

Label design for liquor bottle. Designers may submit multiple submissions.

Product Description:
Name: Luna de Cobre™
Alcohol Category: Aguardiente (which in Spanish most closely translates to “burning water”) – aguardiente is derived from
cane sugar and is a general term for a type of alcoholic spirit in many Central and South America countries.
Taste: A smooth liquor with a comfortable yet spicy finish
Smell: Subtle aroma of spicy jalapeños
Liquid Color: Clear
Bottle Color: Clear
See link for reference - http://www.pellowinery.example/sites/default/files/styles/uc_product_full/public/Vessel_0.jpg?itok=8KqTm2Xw
Closure: Bar top / cork
Bottle Shape/Size: height = 8.67in; diameter of base = 3.70in; diameter of neck = 0.85in

Label may consist of two separate parts (i.e. front and back, front and vertical side), or one continuous label.

Designer has complete freedom with color, font etc. unless otherwise stated below. The label MUST
contain (but is not limited only to) the following text exactly as written in quotes below:
- “Luna de Cobre”
- “Aguardiente”
- “Cane Neutral Spirit with Natural Flavors”
- “35% Alc./Vol.”
- “750 ml”
- “Bottled by QM Spirits, LLC” and “Nashville, TN” - “Government Warning: (1) According to the Surgeon General, women should not drink alcoholic beverages during
pregnancy because of the risk of birth defects. (2) Consumption of alcoholic beverages impairs your ability to
drive a car or operate machinery, and may cause health problems.” (text in previous quotes must be in all
capitalized letters, text must be 2 MM in height and quote must be separated 2MM by all other text)
- Must be dedicated empty space for bar code (approximately 0.75in. height x 1.25in. length)
Updates

Target Market(s)

Label should have mass market appeal.
Age: 21 – 28 years old (primary target market is 21+ year old college students and recent graduates)
Target Market Gender: Both male and female, with emphasis on male
Consumption Focus: Spirit will be consumed typically as a shot, primarily at bars and secondarily off premise (label design will be critical for making our product highly visible behind a bar)
Marketing Theme: South American elements. The official Luna de Cobre mascot is a llama and the incorporation and use of a llama somewhere (however large or small) on the bottle is encourage but by no means required.

Industry/Entity Type

Health

Requirements
Should not have
• Elements that may lead a potential consumer to believe the beverage is a craft liquor or an artisan brand. Please do not include images of peppers.

```html
<!DOCTYPE html>
<html lang="en">
<head>
<meta charset="UTF-8">
<title>Luna de Cobre™ Aguardiente Label</title>
<link href="https://fonts.googleapis.com/css2?family=Oswald:wght@500&family=Oleo+Script:wght@700&family=Josefin+Sans:wght@300;400&family=Open+Sans:wght@400;600&display=swap" rel="stylesheet">
<style>
  :root {
    --backdrop: #cfcfcf;
    --paper: #ddd3c0;
    --ink: #3d342b;
    --fire-red: #c8282d;
    --flame: #d98d80;
    --flame-soft: #e8c4b2;
    --white: #ffffff;
  }
  * { box-sizing: border-box; margin: 0; padding: 0; }
  html, body { width: 1200px; height: 851px; overflow: hidden; }
  body { background: var(--backdrop); position: relative; font-family: "Open Sans", sans-serif; color: var(--ink); }

  .front-label {
    position: absolute; left: 340px; top: 40px; width: 520px; height: 657px;
    background: var(--paper); overflow: hidden;
  }
  .front-label__band { position: absolute; left: 0; width: 100%; background: var(--ink); }
  .front-label__band--top { top: 0; height: 15px; }
  .front-label__band--bottom { bottom: 0; height: 13px; }

  .flame-field {
    position: absolute; right: 0; top: 15px; width: 290px; height: 629px;
    background: linear-gradient(100deg, rgba(232,196,178,0) 0%, var(--flame-soft) 35%, var(--flame) 80%, var(--flame-soft) 100%);
    opacity: .75;
  }

  .brand-row {
    position: absolute; top: 19px; left: 0; width: 100%; height: 105px;
    display: flex; justify-content: center; align-items: flex-end; gap: 10px;
  }
  .brand-name { font-family: "Oswald", sans-serif; font-weight: 500; font-size: 24px; line-height: 1; color: var(--ink); padding-bottom: 4px; }
  .mascot-art {
    width: 81px; height: 105px;
    background: linear-gradient(160deg, var(--fire-red), #8e1d1f);
    border: 2px solid var(--ink);
  }

  .product-title {
    position: absolute; top: 165px; left: 0; width: 100%; text-align: center;
    font-family: "Oleo Script", cursive; font-weight: 700; font-size: 86px; line-height: 1;
    color: var(--ink); letter-spacing: -1px; padding-left: 6px; white-space: nowrap;
    text-shadow: -4px 3px 0 var(--fire-red);
  }
  .product-desc {
    position: absolute; top: 300px; left: 0; width: 100%; text-align: center;
    font-family: "Josefin Sans", sans-serif; font-weight: 400; font-size: 15px; letter-spacing: .5px; text-transform: uppercase;
  }
  .rule { position: absolute; left: 40px; width: 440px; height: 1px; background: var(--ink); }
  .rule--top { top: 364px; }
  .rule--bottom { top: 419px; }
  .measures {
    position: absolute; top: 378px; left: 0; width: 100%;
    display: flex; justify-content: center; align-items: center; gap: 22px;
    font-family: "Josefin Sans", sans-serif; font-weight: 300; font-size: 20px; text-transform: uppercase;
  }
  .measures__divider { width: 1px; height: 28px; background: var(--ink); }
  .bottler {
    position: absolute; top: 438px; left: 0; width: 100%; text-align: center;
    font-family: "Oswald", sans-serif; font-weight: 500; font-size: 9px; letter-spacing: .4px; text-transform: uppercase;
  }
  .warning {
    position: absolute; top: 489px; left: 44px; width: 262px;
    font-size: 11.5px; line-height: 1.6; color: var(--ink);
  }
  .warning strong { font-weight: 600; }
  .warning-divider { position: absolute; left: 328px; top: 497px; width: 1px; height: 115px; background: var(--ink); }
  .barcode-space { position: absolute; left: 397px; top: 499px; width: 79px; height: 117px; background: var(--white); }

  .neck-label {
    position: absolute; left: 220px; top: 752px; width: 760px; height: 75px;
    background: var(--paper); display: flex; overflow: hidden;
  }
  .neck-label__end {
    width: 172px; height: 100%; background: var(--ink); color: var(--paper);
    display: flex; align-items: center; justify-content: center;
    font-family: "Oswald", sans-serif; font-weight: 500; font-size: 21px; white-space: nowrap; position: relative; z-index: 1;
  }
  .neck-label__middle { flex: 1; position: relative; display: flex; justify-content: center; align-items: center; }
  .neck-flames {
    position: absolute; inset: 0;
    background: linear-gradient(90deg, var(--paper) 0%, var(--flame-soft) 30%, var(--flame) 50%, var(--flame-soft) 70%, var(--paper) 100%);
    opacity: .7;
  }
  .neck-mascot {
    position: relative; width: 90px; height: 75px;
    background: linear-gradient(160deg, var(--fire-red), #8e1d1f);
    border-left: 2px solid var(--ink); border-right: 2px solid var(--ink);
  }
</style>
</head>
<body>
  <section class="front-label">
    <div class="front-label__band front-label__band--top"></div>
    <div class="flame-field" role="img" aria-label="Flowing flame pattern in soft red and cream"></div>

    <div class="brand-row">
      <span class="brand-name">LUNA DE</span>
      <div class="mascot-art" role="img" aria-label="Llama mascot illustration on a red burst panel"></div>
      <span class="brand-name">COBRE™</span>
    </div>

    <h1 class="product-title">Aguardiente</h1>
    <p class="product-desc">Cane Neutral Spirit with Natural Flavors</p>

    <div class="rule rule--top"></div>
    <div class="measures">
      <span>750 ml</span>
      <span class="measures__divider"></span>
      <span>35% Alc./Vol.</span>
    </div>
    <div class="rule rule--bottom"></div>

    <p class="bottler">Bottled by QM Spirits, LLC &amp; Nashville, TN</p>

    <p class="warning"><strong>Government Warning:</strong><br>According to the Surgeon General, women should not drink alcoholic beverages during pregnancy because of the risk of birth defects. Consumption of alcoholic beverages impairs your ability to drive a car or operate machinery, and may cause health problems.</p>
    <div class="warning-divider"></div>
    <div class="barcode-space"></div>

    <div class="front-label__band front-label__band--bottom"></div>
  </section>

  <section class="neck-label">
    <div class="neck-label__end">LUNA DE COBRE™</div>
    <div class="neck-label__middle">
      <div class="neck-flames" role="img" aria-label="Flowing flame pattern in soft red and cream"></div>
      <div class="neck-mascot" role="img" aria-label="Llama mascot illustration on a red burst panel"></div>
    </div>
    <div class="neck-label__end">LUNA DE COBRE™</div>
  </section>
</body>
</html>
```